Zanquerra Business Card Design

Zanquerra is a small and new restaurant/ bar location in Hong Kong. The name "Djibouti" derives from an African country. There is no specific reason behind other than the fact, that the bar is somewhat inspired by African elements (only inspired but not purely based on African cuisine etc.).

The bar is somewhat a fusion of African, Mediterranean and Oriental (Old French Vietnam) elements.

However, it is very imperative to stress, that the overall look and feel of Zanquerra is a very high end cocktail lounge/ bar location. The bar is tucked away in a hidden alley, so people will have to know about it. The idea is to send the consumer off in an Escape or hidden remote location where they are at ease in a hip, stylish and trendy environment.

The card needs to feel high-end.

Final logo artwork has been attached and also pictures of the bar/ restaurant itself. The logo ie monkey head cannot be modified. However, the background color and the color of the type "ZANQUERRA" can be changed.

The following details need to fit onto the business card. Of course they can be arranged to your liking:

LOGO

Tobin Le
Partner

+852 90817364
xxx@zanquerra-bar.com
www.zanquerra-bar.com
4C, Pelham Lane, Wan Chai, Hong Kong

Industry/Entity Type

Restaurant

```html
<!DOCTYPE html>
<html lang="en">
<head>
<meta charset="UTF-8">
<title>Zanquerra Business Card</title>
<link rel="stylesheet" href="https://fonts.googleapis.com/css2?family=Fira+Sans:wght@400;500&display=swap">
<style>
  :root {
    --stage: #d9d9d6;
    --brand-red: #e3161c;
    --brand-red-deep: #c70f15;
    --name-tint: #f4d3d3;
    --paper: #ffffff;
    --paper-shade: #e4e4e4;
    --ink: #1a1a1a;
    --accent: #b3121a;
    --disc: #ffffff;
  }
  * { box-sizing: border-box; margin: 0; padding: 0; }
  html, body {
    width: 1200px; height: 1000px; overflow: hidden;
    background: var(--stage);
    font-family: "Fira Sans", Arial, sans-serif;
  }
  .canvas {
    position: relative; width: 1200px; height: 1000px;
  }
  .card {
    position: absolute; top: 184px;
    width: 380px; height: 633px;
    overflow: hidden;
    box-shadow: 0 10px 30px rgba(0,0,0,0.18);
  }
  /* Front */
  .card-front { left: 150px; background: var(--brand-red); }
  .front-pattern {
    position: absolute; inset: 0;
    background:
      radial-gradient(circle at 62% 30%, rgba(255,255,255,0.35) 0, rgba(255,255,255,0) 32%),
      linear-gradient(160deg, var(--brand-red) 0%, var(--brand-red-deep) 100%);
  }
  .front-disc {
    position: absolute; left: 160px; top: 110px;
    width: 160px; height: 160px; border-radius: 50%;
    background: var(--disc);
    border: 6px solid #111;
  }
  .front-name {
    position: absolute; left: 118px; top: 200px;
    transform: rotate(90deg); transform-origin: top left;
    font-size: 60px; font-weight: 400; letter-spacing: 4px;
    color: var(--name-tint); white-space: nowrap; line-height: 1;
  }
  /* Back */
  .card-back { left: 670px; background: linear-gradient(180deg, var(--paper-shade) 0%, var(--paper) 55%, var(--paper-shade) 100%); }
  .back-emblem {
    position: absolute; left: 20px; top: 0; width: 330px; height: 340px;
    border-radius: 0 0 50% 50%;
    background: radial-gradient(ellipse at 50% 35%, rgba(180,180,180,0.35) 0, rgba(200,200,200,0.1) 70%, rgba(255,255,255,0) 100%);
  }
  .details {
    position: absolute; left: 345px; top: 70px;
    transform: rotate(90deg); transform-origin: top left;
    white-space: nowrap; color: var(--ink);
  }
  .details .person { margin-left: 70px; font-size: 19px; line-height: 1.2; }
  .details .role { margin-left: 70px; font-size: 14px; color: var(--accent); margin-bottom: 2px; }
  .details .line { font-size: 19px; line-height: 1.2; }
  .details .prefix { color: var(--accent); }
  .details .address { margin-top: 20px; font-size: 16px; color: var(--accent); }
</style>
</head>
<body>
<main class="canvas">
  <section class="card card-front">
    <div class="front-pattern" role="img" aria-label="Faint repeating pattern of round emblems on red"></div>
    <div class="front-disc"></div>
    <div class="front-name">ZANQUERRA</div>
  </section>

  <section class="card card-back">
    <div class="back-emblem" role="img" aria-label="Large faint grey brand emblem decoration"></div>
    <div class="details">
      <p class="person">Tobin Le</p>
      <p class="role">Partner</p>
      <p class="line"><span class="prefix">+852</span> 90817364</p>
      <p class="line">xxx@zanquerra-bar.com</p>
      <p class="line">www.zanquerra-bar.com</p>
      <p class="address">4C, Pelham Lane, Wan Chai, Hong Kong</p>
    </div>
  </section>
</main>
</body>
</html>
```